We Need a Letterhead + Fax Cover Sheet for Kestrel Works

LETTERHEAD:
- Simple letterhead. Please provide an editable .doc file apart from usual Source Files. Logo Files attached for your use.
- Please place our logo on the upper right corner of the page. You may add some sort of graphic, or light colored background (depends on what looks good).
- Footer should include:
Kestrel Works, LLC
418 Wrenfield Ave. Suite 172
Mobile, AL 36619

FAX COVER SHEET:
- Have the logo placed here, should be large, maybe an eight of the page.
- Put:
From:
To:
Phone Number:
Fax Number:

*Still needs some details, will update you because working on the website, etc.

Kestrel Harbor Staffing Services

```html
<!DOCTYPE html>
<html lang="en">
<head>
<meta charset="utf-8">
<title>Kestrel Works – Letterhead and Fax Cover Sheet</title>
<link href="https://fonts.googleapis.com/css2?family=Open+Sans:wght@400;600&display=swap" rel="stylesheet">
<style>
  :root {
    --bg: #e4e4e4;
    --paper: #ffffff;
    --ink: #222222;
    --label: #2a2a2a;
    --blue: #1a7bbf;
    --green: #7fa23a;
    --rule: #d6dfc4;
    --dots: #777777;
    --watermark: #f1f1f1;
  }
  * { box-sizing: border-box; margin: 0; padding: 0; }
  html, body { width: 1200px; height: 1200px; overflow: hidden; }
  body {
    background: var(--bg);
    font-family: "Open Sans", sans-serif;
    color: var(--ink);
    position: relative;
  }
  .sheet {
    position: absolute;
    width: 524px;
    height: 733px;
    background: var(--paper);
  }
  .sheet--letterhead { left: 64px; top: 61px; }
  .sheet--fax { left: 623px; top: 398px; }

  .sheet-label {
    position: absolute;
    font-size: 27px;
    letter-spacing: 0.5px;
    color: var(--label);
    text-align: center;
  }
  .sheet-label--letterhead { left: 64px; width: 488px; top: 838px; }
  .sheet-label--fax { left: 623px; width: 524px; top: 340px; }

  .brand-mark {
    position: absolute;
    left: 0; right: 0; top: 28px;
    display: flex; flex-direction: column; align-items: center;
    gap: 6px;
  }
  .brand-mark__dot {
    width: 22px; height: 22px; border-radius: 50%;
    background: var(--blue);
  }
  .brand-mark__name {
    width: 120px;
    text-align: center;
    font-size: 13px;
    font-weight: 600;
    line-height: 1.25;
    color: var(--blue);
  }

  .watermark {
    position: absolute;
    left: 62px; top: 204px;
    width: 400px; height: 330px;
    border-radius: 50%;
    border: 16px solid var(--watermark);
  }
  .sheet--fax .watermark { left: 62px; top: 197px; }

  .footer {
    position: absolute;
    left: 24px; right: 24px;
    bottom: 28px;
    text-align: center;
  }
  .footer__name {
    display: flex; align-items: center; gap: 8px;
    font-size: 15px;
  }
  .footer__name::before, .footer__name::after {
    content: ""; flex: 1; height: 1px; background: var(--rule);
  }
  .footer__name .first { color: var(--blue); }
  .footer__name .rest { color: var(--green); }
  .footer__address { font-size: 13px; margin-top: 6px; letter-spacing: 0.2px; }

  .fax-title {
    position: absolute;
    left: 116px; right: 102px; top: 168px;
    text-align: center;
    font-size: 24px;
    letter-spacing: 3px;
    color: var(--green);
    padding-bottom: 6px;
    border-bottom: 1px solid var(--rule);
  }
  .fax-fields {
    position: absolute;
    left: 44px; right: 32px; top: 262px;
    font-size: 13px;
    letter-spacing: 0.3px;
  }
  .fax-row { display: flex; gap: 12px; margin-bottom: 18px; }
  .fax-row--gap { margin-top: 32px; margin-bottom: 26px; }
  .fax-field { flex: 1; display: flex; align-items: baseline; gap: 4px; }
  .fax-field__line {
    flex: 1; border-bottom: 1px dotted var(--dots); transform: translateY(-3px);
  }
</style>
</head>
<body>

  <section class="sheet sheet--letterhead">
    <div class="watermark" role="img" aria-label="Faint brand emblem background decoration"></div>
    <div class="brand-mark">
      <span class="brand-mark__dot"></span>
      <span class="brand-mark__name">Kestrel Harbor Staffing Services</span>
    </div>
    <footer class="footer">
      <p class="footer__name"><span><span class="first">Kestrel</span> <span class="rest">Works, LLC</span></span></p>
      <p class="footer__address">418 Wrenfield Ave. Suite 172, Mobile, AL 36619</p>
    </footer>
  </section>
  <p class="sheet-label sheet-label--letterhead">LETTERHEAD</p>

  <p class="sheet-label sheet-label--fax">FAX COVER SHEET</p>
  <section class="sheet sheet--fax">
    <div class="watermark" role="img" aria-label="Faint brand emblem background decoration"></div>
    <div class="brand-mark">
      <span class="brand-mark__dot"></span>
      <span class="brand-mark__name">Kestrel Harbor Staffing Services</span>
    </div>
    <h1 class="fax-title" style="font-weight:400">FAX COVER SHEET</h1>
    <div class="fax-fields">
      <div class="fax-row"><div class="fax-field">To <span class="fax-field__line"></span></div></div>
      <div class="fax-row"><div class="fax-field">From <span class="fax-field__line"></span></div></div>
      <div class="fax-row"><div class="fax-field">Re <span class="fax-field__line"></span></div></div>
      <div class="fax-row fax-row--gap">
        <div class="fax-field">Fax Number <span class="fax-field__line"></span></div>
        <div class="fax-field">Pages <span class="fax-field__line"></span></div>
      </div>
      <div class="fax-row">
        <div class="fax-field">Phone Number <span class="fax-field__line"></span></div>
        <div class="fax-field" style="flex:0.75">Date <span class="fax-field__line"></span></div>
      </div>
    </div>
    <footer class="footer">
      <p class="footer__name"><span><span class="first">Kestrel</span> <span class="rest">Works, LLC</span></span></p>
      <p class="footer__address">418 Wrenfield Ave. Suite 172, Mobile, AL 36619</p>
    </footer>
  </section>

</body>
</html>
```